Consulting Group Website Landing Page Design

We are working with a Consulting Group in California. They provide consulting services to law enforcement agencies throughout the US.
Some sites to use for content:
https://www.wardmerecollegium.org
https://www.kfarrelteam.com
https://www.48qzadvisory.com
https://www.vlx.org
http://www.thorvikteam.com
Thank you for taking the time to consider designing a website for us. We are web developers based in Stockton, CA, USA. Most of our projects go through the same process. Understanding this process may help you win a project with us. We custom-code all of our websites in-house. We don’t have any requirements as to what tools you use for your design, but we ask that you follow these guidelines. Plus, please send your designs in at least 1200px. wide so they do not pixelate when we show the client.
IMAGES:
If you use any images or icons in the design, we ask that you have a link to the asset so we can purchase the image/icon. Most of the designs we submit do not have the customer’s images on them unless they have some great images. Be creative; show us the feeling you are trying to portray with your image choices. Use any royalty-free site you choose. We subscribe to Quillet and mainly use their images, but we can purchase images outside of Quillet. PLEASE NOTE: we will not submit designs to clients with watermarks on the images.
FONTS:
We ask that you identify the fonts you’re using in the design. This can be done in a message if you want. We typically use Brivo Fonts and Quillet Fonts.
CONTENT:
We're always open to different content and ideas. We often submit designs with stock images so the client can see our vision. We typically take pictures after the website launch to use their images with our vision. Lorem Ipsum is fine for paragraphs, but we ask that you make the Headers with correct English. We want to be able to show the vision and identify the sections of the website.
INSPIRATION:
We typically add a couple of links in the brief of websites we like to help you get started in your design.
REVISIONS:
We do not often ask for revisions of the designs unless we see something in the design that may not appeal to the client. If there are slight changes that we want to make, we do that in the development process.
FEEDBACK:
We rarely give feedback on designs during the design process. We are working on many website projects and do not have the time to provide feedback. We usually respond if your request is well thought out and asks specific questions, but a note asking “feedback, please” usually goes unanswered.
Number of Pages Required
1 page
Look and feel
Each slider illustrates characteristics of the customer's brand and the style your logo design should communicate.

```html
<!DOCTYPE html>
<html lang="en">
<head>
<meta charset="utf-8">
<title>Corvane Consulting — Police &amp; Public Practices Consulting</title>
<link href="https://fonts.googleapis.com/css2?family=Poppins:wght@400;500;600;700&family=Roboto:wght@400;500;700&family=PT+Serif:wght@400;700&display=swap" rel="stylesheet">
<style>
:root{
  --green:#6bad2b;
  --blue:#0b4191;
  --navy:#0d1a2b;
  --dark:#1f2127;
  --ink:#1d1d1f;
  --muted:#6f7378;
  --soft:#f5f7fa;
  --field:#f1f3f6;
  --white:#ffffff;
}
*{margin:0;padding:0;box-sizing:border-box}
html,body{width:1200px;height:4507px;overflow:hidden;background:var(--white)}
.page{position:relative;width:1200px;height:4507px;overflow:hidden;font-family:"PT Serif",serif;color:var(--ink)}
.abs{position:absolute}
.sans{font-family:"Roboto",sans-serif}
.head{font-family:"Poppins",sans-serif}
.btn{position:absolute;display:flex;align-items:center;justify-content:center;background:var(--green);color:var(--white);font:700 13px "Roboto",sans-serif;border-radius:2px}

/* header + hero */
.hero{position:absolute;left:0;top:0;width:1200px;height:682px;clip-path:polygon(0 0,100% 0,100% 682px,0 569px);
  background:radial-gradient(ellipse at 70% 40%,#2b3a4c 0%,#121c29 55%,#0a111b 100%)}
.brand{position:absolute;display:flex;align-items:center;gap:8px;color:var(--white);font:600 20px "Poppins",sans-serif}
.brand .dot{width:26px;height:26px;border-radius:50%;border:4px solid var(--blue);background:var(--green)}
.nav{position:absolute;top:34px;font:500 14px "Roboto",sans-serif;color:var(--white)}
.nav.active{color:var(--green)}
.hero-title{position:absolute;left:0;width:1200px;top:232px;text-align:center;color:var(--white);font:600 62px/64px "Poppins",sans-serif;letter-spacing:-1px}
.hero-text{position:absolute;left:190px;width:820px;top:385px;text-align:center;color:var(--white);font-size:15px;line-height:23px}

/* section labels */
.label{position:absolute;display:flex;align-items:center}
.label i{display:block;height:2px;background:var(--blue)}
.label span{background:var(--blue);color:var(--white);font:500 17px/24px "Roboto",sans-serif;padding:0 10px}
.h2{position:absolute;color:var(--green);font:500 42px/44px "Poppins",sans-serif}
.body{position:absolute;color:var(--muted);font-size:15px;line-height:22.5px}

/* CTA band */
.band{position:absolute;left:0;top:1251px;width:1200px;height:708px;clip-path:polygon(0 0,100% 0,100% 100%,0 598px);
  background:radial-gradient(ellipse at 45% 45%,#2f3a48 0%,#141d29 60%,#0a111a 100%)}
.band h3{position:absolute;left:0;width:1200px;top:240px;text-align:center;color:var(--white);font:400 41px/44px "Poppins",sans-serif}
.band p{position:absolute;left:300px;width:600px;top:350px;text-align:center;color:var(--white);font-size:15px;line-height:23px}

/* services */
.services{position:absolute;left:0;top:1849px;width:1200px;height:888px;background:var(--soft)}
.card{position:absolute;top:2230px;width:238px;height:411px;background:var(--white);border-bottom:3px solid var(--green);box-shadow:0 6px 20px rgba(20,30,50,.08);text-align:center}
.card .pic{position:absolute;left:53px;top:23px;width:132px;height:132px;border-radius:50%;border:6px solid var(--blue)}
.card h4{position:absolute;left:10px;right:10px;top:178px;font:500 20px/23px "Poppins",sans-serif;color:var(--ink)}
.card p{position:absolute;left:18px;right:18px;color:var(--muted);font-size:14.5px;line-height:22px}

/* contact */
.contact{position:absolute;left:0;top:2737px;width:600px;height:604px;background:var(--white);border-bottom:4px solid var(--green);box-shadow:0 0 18px rgba(0,0,0,.05)}
.field{position:absolute;background:var(--field);border:1px solid #e7eaee;color:#9a9ea4;font:400 13px "Roboto",sans-serif;padding:0 14px;display:flex;align-items:center}
.contact-photo{position:absolute;left:600px;top:2755px;width:600px;height:568px;background:linear-gradient(135deg,#7c6651 0%,#4c5f78 55%,#2f4a72 100%)}

/* reviews */
.review{position:absolute;top:3598px;width:318px;height:215px;border:1px solid #e3e6ea;background:var(--white)}
.review p{position:absolute;left:18px;right:18px;top:20px;font:400 12.5px/21px "Roboto",sans-serif;color:#55595e}
.avatar{position:absolute;left:18px;top:128px;width:64px;height:64px;border-radius:50%;border:3px solid var(--green);background:linear-gradient(160deg,#c9ccd2,#6b7380)}
.review b{position:absolute;left:100px;top:144px;font:700 15px "PT Serif",serif;color:var(--ink)}
.review em{position:absolute;left:100px;top:166px;font:400 13px "PT Serif",serif;font-style:normal;color:var(--muted)}
.dots{position:absolute;top:3830px;left:575px;display:flex;gap:12px}
.dots i{width:9px;height:9px;border-radius:50%;background:#9fb0c7}
.dots i.on{background:var(--green)}

/* footer */
.footer{position:absolute;left:0;top:3984px;width:1200px;height:523px;background:var(--dark);clip-path:polygon(0 117px,100% 0,100% 100%,0 100%);color:var(--white)}
.fcol h5{position:absolute;font:600 17px "Poppins",sans-serif;color:var(--white)}
.fcol h5::after{content:"";display:inline-block;width:18px;height:3px;background:var(--green);margin-left:6px;vertical-align:-3px}
.fcol a{position:absolute;font:400 14px "Poppins",sans-serif;color:#e6e7ea;text-decoration:none}
.social{position:absolute;width:14px;height:14px;border-radius:50%;border:2px solid var(--white)}
.rule{position:absolute;left:0;top:4445px;width:1200px;height:1px;background:#34373f}
</style>
</head>
<body>
<div class="page">

  <!-- Hero -->
  <div class="hero" role="img" aria-label="Night-time photo of police officers beside a patrol car, darkened"></div>
  <div class="brand" style="left:62px;top:28px"><span class="dot"></span>Corvane Consulting</div>
  <span class="nav active" style="left:399px">Home</span>
  <span class="nav" style="left:485px">About Us</span>
  <span class="nav" style="left:594px">Services</span>
  <span class="nav" style="left:698px">Contact Us</span>
  <div class="btn" style="left:968px;top:23px;width:169px;height:43px;font-size:14px">
    <svg width="14" height="14" viewBox="0 0 24 24" style="margin-right:6px"><path fill="#fff" d="M6.6 10.8a15.1 15.1 0 0 0 6.6 6.6l2.2-2.2c.3-.3.7-.4 1-.2 1.1.4 2.3.6 3.6.6.6 0 1 .4 1 1V20c0 .6-.4 1-1 1A17 17 0 0 1 3 4c0-.6.4-1 1-1h3.5c.6 0 1 .4 1 1 0 1.3.2 2.5.6 3.6.1.3 0 .7-.2 1z"/></svg>
    (555) 010 4567
  </div>
  <h1 class="hero-title">Police &amp; Public Practices<br>Consulting Services</h1>
  <p class="hero-text">Police and public organizations have all kinds of difficult and extremely complex internal and external challenges thrown your way. You need advice that mitigates risks, protects public investments, and drives maximum value to community stakeholders.</p>
  <div class="btn" style="left:495px;top:472px;width:203px;height:48px">Make an Appointment</div>

  <!-- About -->
  <div class="label" style="left:108px;top:786px"><i style="width:74px"></i><span>ABOUT US</span></div>
  <h2 class="h2" style="left:108px;top:828px">Police &amp; Public Practices<br>Consulting Services</h2>
  <p class="body" style="left:108px;top:933px;width:480px">Integer luctus duis iaculis consequat arcu tortor. Convallis curae primis massa in aenean dui hendrerit. Gravida nostra vel at leo porta mattis montes congue dictumst arcu. Quis enim etiam cras potenti integer ut erat vestibulum orci maecenas. Sodales efficitur senectus amet ut malesuada scelerisque elit finibus.</p>
  <div class="btn" style="left:108px;top:1079px;width:144px;height:44px">Discover More</div>
  <svg class="abs" style="left:680px;top:770px" width="385" height="380" viewBox="0 0 385 380">
    <circle cx="190" cy="188" r="168" fill="#d9d5cf"/>
    <path d="M190 20 A168 168 0 1 0 358 188" fill="none" stroke="#0b4191" stroke-width="17"/>
    <path d="M190 20 A168 168 0 0 1 300 62" fill="none" stroke="#0b4191" stroke-width="17"/>
    <polygon points="290,40 330,72 284,88" fill="#0b4191"/>
    <polygon points="345,170 380,190 352,212" fill="#0b4191"/>
    <polygon points="300,330 335,340 310,372" fill="#0b4191"/>
  </svg>
  <div class="abs" role="img" aria-label="Photo of a consultant working at a desk with colleagues" style="left:702px;top:790px;width:336px;height:336px;border-radius:50%;background:linear-gradient(150deg,#ecebe8 0%,#c9c1b5 60%,#9c8a74 100%)"></div>

  <!-- CTA band -->
  <div class="band" role="img" aria-label="Night-time photo of an officer near a patrol car, darkened">
    <h3>Leading innovators in<br>building trust and respect</h3>
    <p>Lorem ipsum dolor sit amet, consectetur adipiscing elit. Ut elit tellus, luctus nec ullamcorper mattis, pulvinar dapibus leo.</p>
  </div>
  <div class="btn" style="left:525px;top:1679px;width:152px;height:44px">Contact Us Now</div>

  <!-- Services -->
  <div class="services"></div>
  <div class="label" style="left:100px;top:2047px"><i style="width:84px"></i><span>OUR SERVICES</span></div>
  <h2 class="h2" style="left:100px;top:2091px">Public Safety Advisers</h2>
  <p class="body" style="left:100px;top:2153px;width:1000px;font-size:14.5px">Eu netus tellus habitasse nibh malesuada. Rutrum vestibulum turpis faucibus suspendisse non vehicula integer id.</p>

  <div class="card" style="left:94px">
    <div class="pic" role="img" aria-label="Photo of an investigator at work" style="background:linear-gradient(150deg,#eee,#b9ad9c)"></div>
    <h4>Independent<br>Investigations</h4>
    <p style="top:242px">Ultricies porttitor diam urna nisi efficitur magna mollis nunc taciti pulvinar. Nam at nisi dui id facilisis sapien luctus congue euismod aptent lobortis.</p>
  </div>
  <div class="card" style="left:353px">
    <div class="pic" role="img" aria-label="Photo of a public safety officer's back" style="background:linear-gradient(150deg,#d8342a,#1b1b1e)"></div>
    <h4>Public Safety</h4>
    <p style="top:220px">Ultricies porttitor diam urna nisi efficitur magna mollis nunc taciti pulvinar. Nam at nisi dui id facilisis sapien luctus congue euismod aptent lobortis.</p>
  </div>
  <div class="card" style="left:610px">
    <div class="pic" role="img" aria-label="Photo of an analyst reviewing documents" style="background:linear-gradient(150deg,#6d6f76,#2a2c33)"></div>
    <h4>Systems<br>Assessment</h4>
    <p style="top:242px">Ultricies porttitor diam urna nisi efficitur magna mollis nunc taciti pulvinar. Nam at nisi dui id facilisis sapien luctus congue euismod aptent lobortis.</p>
  </div>
  <div class="card" style="left:867px">
    <div class="pic" role="img" aria-label="Photo of officers at night" style="background:linear-gradient(150deg,#4b5a6c,#161f2b)"></div>
    <h4>Policy Analysis</h4>
    <p style="top:220px">Ultricies porttitor diam urna nisi efficitur magna mollis nunc taciti pulvinar. Nam at nisi dui id facilisis sapien luctus congue euismod aptent lobortis.</p>
  </div>

  <!-- Contact -->
  <div class="contact"></div>
  <div class="contact-photo" role="img" aria-label="Photo of a smiling consultant holding a clipboard in an office"></div>
  <div class="label" style="left:45px;top:2849px"><i style="width:76px"></i><span>CONTACT US</span></div>
  <h2 class="h2" style="left:45px;top:2892px">Make your appointment</h2>
  <div class="field" style="left:45px;top:2958px;width:250px;height:40px">Name</div>
  <div class="field" style="left:306px;top:2958px;width:250px;height:40px">Phone</div>
  <div class="field" style="left:45px;top:3010px;width:250px;height:42px">Email</div>
  <div class="field" style="left:306px;top:3010px;width:250px;height:42px;color:#55595e;font-family:'PT Serif',serif;font-size:14px;justify-content:space-between">Financial Technology
    <svg width="10" height="6" viewBox="0 0 10 6"><polygon points="0,0 10,0 5,6" fill="#55595e"/></svg></div>
  <div class="field" style="left:45px;top:3063px;width:511px;height:96px;align-items:flex-start;padding-top:12px">Message</div>
  <div class="btn" style="left:45px;top:3169px;width:511px;height:49px">Make an Appointment</div>

  <!-- Reviews -->
  <div class="label" style="left:84px;top:3449px"><i style="width:132px"></i><span>OUR SERVICES</span></div>
  <h2 class="h2" style="left:84px;top:3492px">Our Clients Reviews</h2>
  <div class="abs" style="left:955px;top:3494px;width:95px;height:2px;background:#b9c6d8"></div>
  <svg class="abs" style="left:1063px;top:3481px" width="46" height="32" viewBox="0 0 46 32">
    <path fill="#6bad2b" d="M0 0h19v17L11 32H3l6-14H0zM26 0h20v17L37 32h-8l7-14h-10z"/>
  </svg>

  <div class="review" style="left:100px">
    <p>"Porttitor integer bibendum odio pulvinar rutrum magnis viverra orci tincidunt efficitur. Aptent pharetra est nunc mattis donec per mi porttitor penatibus."</p>
    <div class="avatar" role="img" aria-label="Client portrait"></div><b>Dorian Pell</b><em>Trader</em>
  </div>
  <div class="review" style="left:441px">
    <p>"Porttitor integer bibendum odio pulvinar rutrum magnis viverra orci tincidunt efficitur. Aptent pharetra est nunc mattis donec per mi porttitor penatibus."</p>
    <div class="avatar" role="img" aria-label="Client portrait"></div><b>Harlan T. Meeks</b><em>Accountant</em>
  </div>
  <div class="review" style="left:782px">
    <p>"Porttitor integer bibendum odio pulvinar rutrum magnis viverra orci tincidunt efficitur. Aptent pharetra est nunc mattis donec per mi porttitor penatibus."</p>
    <div class="avatar" role="img" aria-label="Client portrait"></div><b>Renata L. Oswin</b><em>Manager</em>
  </div>
  <div class="dots"><i></i><i></i><i class="on"></i></div>

  <!-- Footer -->
  <div class="footer"></div>
  <div class="brand" style="left:70px;top:4200px;font-size:26px"><span class="dot" style="width:34px;height:34px"></span>Corvane Consulting</div>
  <div class="abs sans" style="left:64px;top:4278px;color:#fff;font-size:14px;display:flex;align-items:center;gap:8px">
    <svg width="12" height="12" viewBox="0 0 24 24"><path fill="#6bad2b" d="M6.6 10.8a15.1 15.1 0 0 0 6.6 6.6l2.2-2.2c.3-.3.7-.4 1-.2 1.1.4 2.3.6 3.6.6.6 0 1 .4 1 1V20c0 .6-.4 1-1 1A17 17 0 0 1 3 4c0-.6.4-1 1-1h3.5c.6 0 1 .4 1 1 0 1.3.2 2.5.6 3.6.1.3 0 .7-.2 1z"/></svg>555 0100</div>
  <div class="abs sans" style="left:64px;top:4301px;color:#fff;font-size:14px;display:flex;align-items:center;gap:8px">
    <svg width="12" height="10" viewBox="0 0 24 18"><rect width="24" height="18" rx="2" fill="#6bad2b"/><path d="M1 2l11 8 11-8" stroke="#1f2127" stroke-width="2" fill="none"/></svg>info@corvane.example</div>

  <div class="fcol">
    <h5 style="left:435px;top:4180px">Information</h5>
    <a style="left:435px;top:4225px">History</a>
    <a style="left:435px;top:4254px">Contact Us</a>
    <a style="left:435px;top:4283px">Leadership</a>
    <a style="left:435px;top:4312px">Careers</a>
    <a style="left:435px;top:4341px">News &amp; Article</a>

    <h5 style="left:652px;top:4180px">Services</h5>
    <a style="left:652px;top:4225px">Coaching</a>
    <a style="left:652px;top:4254px">Consulting</a>
    <a style="left:652px;top:4283px">Advisory</a>
    <a style="left:652px;top:4312px">Online Course</a>
    <a style="left:652px;top:4341px">Certification</a>

    <h5 style="left:871px;top:4180px">Follow Us</h5>
  </div>
  <span class="social" style="left:872px;top:4225px" aria-label="Social profile"></span>
  <span class="social" style="left:912px;top:4225px" aria-label="Social profile"></span>
  <span class="social" style="left:952px;top:4225px" aria-label="Social profile"></span>
  <span class="social" style="left:992px;top:4225px" aria-label="Social profile"></span>

  <div class="rule"></div>
  <p class="abs head" style="left:64px;top:4470px;color:#d5d7db;font-size:11.5px">Copyright © 2023 Corvane Consulting. All rights reserved.</p>

</div>
</body>
</html>
```